Fernquill Stationary Design
The Ledger Desk Firm
Fernquill Stationary Design -
Creative Brief
Professional
Marla Dempton
3847 W. Harlan Pkwy. Suite 410 Brackenford, QX 00410
mdempton@fernquill.example
www.fernquill.example
We want to be different in our space. Most if not all of our competitors have boring, text-intensive websites. We want to be different. We're agile, nimple, quick, crisp, entrepreneurial, hip/cool.
Logo, Tagline (The Ledger Desk Firm) and our website address (www.fernquill.example) At the end of the day, play around with what looks cool!

```html
<!DOCTYPE html>
<html lang="en">
<head>
<meta charset="utf-8">
<title>Fernquill Stationery Set</title>
<link rel="stylesheet" href="https://fonts.googleapis.com/css2?family=Orbitron:wght@700&family=Open+Sans:wght@400;600&display=swap">
<style>
  :root {
    --board: #2e2f31;
    --paper: #ffffff;
    --ink: #1c1c1c;
    --green: #7dbb2a;
    --green-dark: #5d9419;
    --grey: #8a8d90;
    --grey-light: #e6e8e9;
    --label: #9a9c9e;
  }
  * { box-sizing: border-box; margin: 0; padding: 0; }
  html, body { width: 1200px; height: 372px; overflow: hidden; }
  body {
    background: radial-gradient(ellipse at 50% 40%, #3a3b3d 0%, var(--board) 70%);
    font-family: "Open Sans", sans-serif;
    position: relative;
  }
  .item { position: absolute; background: var(--paper); box-shadow: 0 3px 8px rgba(0,0,0,.55); overflow: hidden; }
  .item svg.art { position: absolute; inset: 0; width: 100%; height: 100%; }
  .label { position: absolute; font-size: 5px; color: var(--label); white-space: nowrap; }
  .brand { position: absolute; display: flex; align-items: center; gap: 3px; z-index: 1; }
  .brand-dot { width: 8px; height: 8px; border-radius: 50%; background: var(--green); flex: none; }
  .brand-name { font-family: "Orbitron", sans-serif; font-weight: 700; color: var(--ink); font-size: 10px; letter-spacing: .3px; line-height: 1; }
  .brand.on-dark .brand-name { color: var(--paper); }
  .tagline { font-size: 4.5px; color: var(--grey); display: block; margin-top: 2px; }
  .contact { position: absolute; font-size: 4px; line-height: 1.45; color: #444; white-space: nowrap; z-index: 1; }
  .contact strong { font-weight: 600; color: var(--ink); font-size: 4.8px; }
  .dark { background: var(--ink); }
  .greenbg { background: var(--green); }
  .emblem { position: absolute; border-radius: 50%; background: radial-gradient(circle, #f2f3f3 0%, #e3e5e6 100%); }
</style>
</head>
<body>

<!-- Business card set 1 -->
<div class="item" style="left:24px;top:36px;width:144px;height:84px;">
  <div class="dark" style="position:absolute;left:0;top:0;width:100%;height:26px;"></div>
  <div class="brand on-dark" style="left:8px;top:9px;"><span class="brand-dot"></span><span class="brand-name">FERNQUILL</span></div>
  <div class="contact" style="left:8px;top:38px;">
    <strong>Marla Dempton</strong><br>3847 W. Harlan Pkwy. Suite 410<br>Brackenford, QX 00410<br>mdempton@fernquill.example<br>www.fernquill.example
  </div>
</div>
<div class="label" style="left:34px;top:124px;">Card front v1</div>

<div class="item" style="left:187px;top:36px;width:137px;height:84px;">
  <svg class="art" viewBox="0 0 137 84" preserveAspectRatio="none">
    <path d="M72 0 C110 18 120 55 137 84 L137 0 Z" fill="var(--green)"/>
    <path d="M62 0 C100 22 114 58 126 84 L137 84 C120 55 110 18 72 0 Z" fill="var(--ink)"/>
  </svg>
  <div class="brand" style="left:10px;top:38px;"><span class="brand-dot"></span><span class="brand-name">FERNQUILL</span></div>
</div>
<div class="label" style="left:230px;top:124px;">Card back v1</div>

<!-- Business card set 2 -->
<div class="item" style="left:24px;top:151px;width:144px;height:72px;">
  <div class="brand" style="left:28px;top:24px;"><span class="brand-dot"></span><span><span class="brand-name">FERNQUILL</span><span class="tagline">The Ledger Desk Firm</span></span></div>
</div>
<div class="label" style="left:34px;top:227px;">Card front v2</div>

<div class="item dark" style="left:187px;top:151px;width:137px;height:72px;">
  <div class="contact" style="left:10px;top:14px;color:#ccc;">
    <strong style="color:var(--green);">Marla Dempton</strong><br>3847 W. Harlan Pkwy. Suite 410<br>Brackenford, QX 00410<br>mdempton@fernquill.example<br>velmorasta
  </div>
</div>
<div class="label" style="left:230px;top:227px;">Card back v2</div>

<!-- Business card set 3 -->
<div class="item" style="left:24px;top:252px;width:144px;height:67px;">
  <div class="brand" style="left:30px;top:28px;"><span class="brand-dot"></span><span class="brand-name">FERNQUILL</span></div>
</div>
<div class="label" style="left:34px;top:323px;">Card front v3</div>

<div class="item greenbg" style="left:187px;top:252px;width:137px;height:67px;">
  <div class="contact" style="left:10px;top:12px;color:#fff;">
    <strong style="color:#fff;">Marla Dempton</strong><br>3847 W. Harlan Pkwy. Suite 410<br>Brackenford, QX 00410<br>www.fernquill.example
  </div>
</div>
<div class="label" style="left:230px;top:323px;">Card back v3</div>

<!-- Letterhead -->
<div class="item" style="left:343px;top:19px;width:161px;height:334px;">
  <div class="brand" style="left:12px;top:14px;"><span class="brand-dot"></span><span class="brand-name">FERNQUILL</span></div>
  <div class="emblem" role="img" aria-label="Faint large circle emblem" style="left:14px;top:120px;width:132px;height:132px;"></div>
  <svg class="art" viewBox="0 0 161 334" preserveAspectRatio="none">
    <path d="M0 282 C50 300 110 302 161 282 L161 334 L0 334 Z" fill="var(--green)"/>
    <path d="M0 275 C50 293 110 295 161 275 L161 282 C110 302 50 300 0 282 Z" fill="var(--ink)"/>
  </svg>
  <div class="contact" style="left:12px;top:318px;color:#fff;">www.fernquill.example</div>
</div>
<div class="label" style="left:398px;top:359px;">Letterhead A4</div>

<!-- Envelope front -->
<div class="item" style="left:595px;top:67px;width:197px;height:96px;">
  <div class="brand" style="left:10px;top:10px;"><span class="brand-dot"></span><span><span class="brand-name">FERNQUILL</span><span class="tagline">The Ledger Desk Firm</span></span></div>
  <svg class="art" viewBox="0 0 197 96" preserveAspectRatio="none">
    <path d="M0 76 C60 62 130 64 197 80 L197 96 L0 96 Z" fill="var(--green)"/>
    <path d="M0 70 C60 56 130 58 197 74 L197 80 C130 64 60 62 0 76 Z" fill="var(--grey)"/>
  </svg>
</div>
<div class="label" style="left:665px;top:167px;">Envelope DL front</div>

<!-- Envelope back -->
<div class="item" style="left:595px;top:199px;width:197px;height:89px;">
  <div class="brand" style="left:10px;top:10px;"><span class="brand-dot"></span><span class="brand-name">FERNQUILL</span></div>
  <svg class="art" viewBox="0 0 197 89" preserveAspectRatio="none">
    <path d="M0 72 C60 58 130 60 197 74 L197 89 L0 89 Z" fill="var(--green)"/>
    <path d="M0 66 C60 52 130 54 197 68 L197 74 C130 60 60 58 0 72 Z" fill="var(--ink)"/>
  </svg>
</div>
<div class="label" style="left:667px;top:292px;">Envelope DL back</div>

<!-- Envelope stack -->
<div class="item" style="left:893px;top:72px;width:276px;height:60px;background:linear-gradient(#5b5e61,#2a2b2d);">
  <svg class="art" viewBox="0 0 276 60" preserveAspectRatio="none">
    <path d="M0 24 L138 56 L276 24 L276 60 L0 60 Z" fill="var(--grey-light)"/>
  </svg>
  <div class="brand" style="left:134px;top:30px;"><span class="brand-dot"></span></div>
</div>
<div class="item" style="left:893px;top:137px;width:276px;height:67px;">
  <svg class="art" viewBox="0 0 276 67" preserveAspectRatio="none">
    <path d="M0 0 L276 0 L276 18 L138 52 L0 18 Z" fill="var(--green)"/>
    <path d="M0 18 L138 52 L276 18" fill="none" stroke="var(--green-dark)" stroke-width="1"/>
  </svg>
  <div class="brand" style="left:134px;top:26px;"><span class="brand-dot" style="background:var(--ink);"></span></div>
</div>
<div class="item" style="left:893px;top:211px;width:276px;height:72px;">
  <svg class="art" viewBox="0 0 276 72" preserveAspectRatio="none">
    <path d="M0 0 L138 42 L276 0" fill="none" stroke="#d5d7d8" stroke-width="1"/>
    <path d="M0 72 L110 34 M276 72 L166 34" fill="none" stroke="#e2e4e5" stroke-width="1"/>
  </svg>
</div>
<div class="label" style="left:1010px;top:290px;">Envelope set</div>

</body>
</html>
```